Design a premium label for the most expensive honey in the world: Manuka honey.

Manuka honey is originaire from New Zealand and recognized for its natural antibacterial activity. Rare and expensive, it is used in hospital as medical grade mainly to cure burns and wounds... Household will use it out of a pot like a "supplement" or to cure all sorts of ailments.
The label must feel:
- Premium and elegant .
- Reflect strongly its origin New Zealand. Use maori design but be careful of copyright. Must be styled.
- Purity and trust it is the real deal. Feel strongly that it is not an ersatz...
- Health and "medical" use.
Label must have:
* Brand: TOROWAI DOWNS
* MANUKA HONEY
* Made in New Zealand
* e250g
* MGO300
Target Market(s)
Export.

```html
<!DOCTYPE html>
<html lang="en">
<head>
<meta charset="utf-8">
<title>Torowai Downs – Manuka Honey Label</title>
<link rel="stylesheet" href="https://fonts.googleapis.com/css2?family=Libre+Caslon+Text:wght@400;700&family=Marcellus&family=Montserrat:wght@600&display=swap">
<style>
  :root {
    --gold: #c9a349;
    --gold-deep: #b8923a;
    --white: #ffffff;
    --frame: #d4d4d6;
    --ink: #111111;
    --black: #000000;
    --blossom-pink: #eda3ae;
    --blossom-pale: #f5f3f1;
  }
  * { margin: 0; padding: 0; box-sizing: border-box; }
  html, body { width: 1200px; height: 1200px; overflow: hidden; background: var(--white); }
  .board { position: relative; width: 1200px; height: 1200px; }
  .centered { position: absolute; transform: translateX(-50%); white-space: nowrap; text-align: center; }

  .version-title {
    font-family: "Marcellus", serif; font-size: 37px; font-weight: 400; letter-spacing: 3px;
    color: var(--ink); top: 30px;
  }

  .label {
    position: absolute; top: 81px; width: 531px; height: 478px;
    border: 2px solid var(--frame); background: var(--white);
    font-family: "Libre Caslon Text", serif; color: var(--gold);
  }
  .label .centered { left: 50%; }
  .label--a { left: 43px; }
  .label--b { left: 607px; }

  .brand { display: flex; align-items: center; gap: 12px; line-height: 1; }
  .brand-dot { width: 34px; height: 34px; border: 2px solid var(--gold); border-radius: 50%; flex: none; }
  .brand-name { font-size: 44px; font-weight: 400; }
  .brand-stack { display: flex; flex-direction: column; align-items: center; gap: 14px; }
  .brand-stack .brand-dot { width: 84px; height: 84px; border-width: 3px; }
  .brand-stack .brand-name { font-size: 30px; }

  .premium { font-size: 24px; letter-spacing: 3px; }
  .product { font-size: 46px; font-weight: 400; letter-spacing: 1px; }
  .rule { position: absolute; height: 3px; width: 200px; background: var(--gold); transform: translateX(-50%); left: 50%; }
  .harvest { font-size: 24px; }
  .origin { font-size: 35px; letter-spacing: 4px; }
  .grade {
    position: absolute; left: 50%; transform: translateX(-50%);
    width: 200px; height: 58px; background: var(--gold); color: var(--white);
    font-size: 35px; display: flex; align-items: center; justify-content: center;
  }
  .weight { font-size: 29px; }

  .rationale-panel { position: absolute; left: 0; top: 600px; width: 1200px; height: 600px; background: var(--black); }
  .jar-photo {
    position: absolute; left: 67px; top: 73px; width: 463px; height: 462px;
    background: linear-gradient(180deg, #34435a 0%, #2b3648 55%, #d8c08e 56%, #e7d2a5 100%);
  }
  .rationale-title {
    position: absolute; left: 566px; top: 70px; width: 570px; text-align: center; white-space: nowrap;
    font-family: "Montserrat", sans-serif; font-weight: 600; font-size: 22px; color: var(--white); letter-spacing: .3px;
  }
  .swatch { position: absolute; width: 86px; height: 86px; }
  .swatch--flower { left: 663px; top: 134px; background: linear-gradient(160deg, var(--blossom-pale) 0%, var(--blossom-pink) 55%, var(--blossom-pale) 100%); }
  .swatch--pattern { left: 663px; top: 274px; background: linear-gradient(135deg, #7a1414, #f3ecd0 50%, #3a0b0b); }
  .swatch--white { left: 663px; top: 413px; background: var(--white); }
  .swatch--gold { left: 922px; top: 413px; background: linear-gradient(180deg, var(--gold), var(--gold-deep)); }
  .caption {
    position: absolute; transform: translateX(-50%); text-align: center; white-space: nowrap;
    font-family: "Montserrat", sans-serif; font-weight: 600; font-size: 16px; line-height: 20px; color: var(--white);
  }
  .mark-display { position: absolute; left: 966px; top: 150px; transform: translateX(-50%); display: flex; flex-direction: column; align-items: center; gap: 16px; }
  .mark-display .brand-dot { width: 150px; height: 150px; border-width: 4px; }
  .mark-display .brand-name { font-family: "Libre Caslon Text", serif; font-size: 30px; color: var(--gold); white-space: nowrap; }
</style>
</head>
<body>
<main class="board">
  <h2 class="version-title centered" style="left:317px">Version A</h2>
  <h2 class="version-title centered" style="left:872px">Version B</h2>

  <section class="label label--a">
    <div class="brand centered" style="top:52px"><span class="brand-dot"></span><span class="brand-name">torowai downs</span></div>
    <p class="premium centered" style="top:136px">PREMIUM</p>
    <h1 class="product centered" style="top:160px">MANUKA HONEY</h1>
    <div class="rule" style="top:235px"></div>
    <p class="harvest centered" style="top:258px">Harvested and certified in</p>
    <p class="origin centered" style="top:288px">NEW ZEALAND</p>
    <div class="grade" style="top:353px">MGO300+</div>
    <p class="weight centered" style="top:424px">E250g</p>
  </section>

  <section class="label label--b">
    <div class="brand brand-stack centered" style="top:22px"><span class="brand-dot"></span><span class="brand-name">torowai downs</span></div>
    <p class="premium centered" style="top:183px">PREMIUM</p>
    <h1 class="product centered" style="top:203px">MANUKA HONEY</h1>
    <div class="rule" style="top:270px"></div>
    <p class="harvest centered" style="top:285px">Harvested and certified in</p>
    <p class="origin centered" style="top:308px">NEW ZEALAND</p>
    <div class="grade" style="top:370px">MGO300+</div>
    <p class="weight centered" style="top:428px">E250g</p>
  </section>

  <section class="rationale-panel">
    <div class="jar-photo" role="img" aria-label="Photograph of the labelled amber honey jar on a wooden shelf"></div>
    <h3 class="rationale-title">RATIONALE FOR LOGO MARK AND LABEL</h3>

    <div class="swatch swatch--flower" role="img" aria-label="Illustration of a pink manuka flower"></div>
    <p class="caption" style="left:706px;top:228px">MANUKA FLOWER</p>
    <div class="swatch swatch--pattern" role="img" aria-label="Maori carved pattern in red, black and cream"></div>
    <p class="caption" style="left:706px;top:370px">MAORI PATTERN</p>
    <div class="swatch swatch--white"></div>
    <p class="caption" style="left:706px;top:508px">WHITE LABEL CONVEYS<br>PURITY</p>
    <div class="swatch swatch--gold"></div>
    <p class="caption" style="left:964px;top:508px">GOLD IS LUXURY</p>

    <div class="mark-display"><span class="brand-dot"></span><span class="brand-name">torowai downs</span></div>
  </section>
</main>
</body>
</html>
```